Bref créative
Torvane
A GroomHaven for Men
Modern
Torvane - A GroomHaven for Men
The Lanterns
Mill Crescent
Ware
KT34 7RW
team@torvane.example
www.torvane.example
Name of Barbers is Torvane
Tag is - A GroomHaven for Men which must feature as part of logo.
GroomHaven is as spelt here (one word - capital B and S)
Use a derivative of the logo
These are the logo eps files. There is also a jpeg file uploaded so you can see the version I require for the design
this is logo version to use but use the eps file version for actual design

```html
<!DOCTYPE html>
<html lang="en">
<head>
<meta charset="utf-8">
<title>Torvane - A GroomHaven for Men</title>
<link rel="stylesheet" href="https://fonts.googleapis.com/css2?family=Arimo:wght@400&display=swap">
<style>
  :root {
    --page: #ffffff;
    --card-light: #ffffff;
    --card-dark: #3a342e;
    --card-edge: #d6d6d2;
    --brand-grey: #8d9184;
    --brand-soft: #c9cbc1;
    --ghost-light: #eeeeea;
    --ghost-dark: #4a453f;
    --ink: #4a4a48;
    --rule: #b9bbb3;
  }
  * { box-sizing: border-box; margin: 0; padding: 0; }
  html, body { width: 1200px; height: 334px; overflow: hidden; background: var(--page); }
  body { font-family: "Arimo", Arial, sans-serif; position: relative; }

  .card { position: absolute; top: 0; width: 588px; height: 334px; overflow: hidden; }
  .card--front { left: 0; background: var(--card-light); border: 1px solid var(--card-edge); }
  .card--back { left: 612px; background: var(--card-dark); }

  .ghost-name {
    position: absolute; left: 190px; top: -34px;
    font-size: 120px; line-height: 1; letter-spacing: 2px;
    color: var(--ghost-light); white-space: nowrap;
  }
  .card--back .ghost-name { color: var(--ghost-dark); }

  .brand { position: absolute; left: 20px; top: 180px; }
  .brand__name {
    display: flex; align-items: center; gap: 10px;
    font-size: 34px; letter-spacing: 1px; color: var(--brand-grey); line-height: 1;
  }
  .brand__mark { width: 14px; height: 14px; background: var(--brand-grey); }
  .brand__tag {
    margin-top: 20px; font-size: 22px; line-height: 1; color: var(--brand-grey); white-space: nowrap;
  }
  .card--back .brand__name,
  .card--back .brand__tag { color: var(--brand-soft); }
  .card--back .brand__mark { background: var(--brand-soft); }

  .divider {
    position: absolute; left: 254px; top: 184px; width: 1px; height: 82px; background: var(--rule);
  }
  .contact {
    position: absolute; left: 266px; top: 188px;
    font-size: 13px; line-height: 17px; color: var(--ink); font-style: normal;
  }
  .contact__gap { display: block; margin-bottom: 6px; }
</style>
</head>
<body>
  <section class="card card--front">
    <div class="ghost-name" aria-hidden="true">torvane</div>
    <div class="brand">
      <div class="brand__name"><span class="brand__mark"></span>torvane</div>
      <p class="brand__tag">A GroomHaven for Men</p>
    </div>
    <div class="divider"></div>
    <address class="contact">
      <span>The Lanterns Mill Crescent</span><br>
      <span class="contact__gap">Ware KT34 7RW</span>
      <span>01632 960418</span><br>
      <span>team@torvane.example</span><br>
      <span>www.torvane.example</span>
    </address>
  </section>

  <section class="card card--back">
    <div class="ghost-name" aria-hidden="true">torvane</div>
    <div class="brand">
      <div class="brand__name"><span class="brand__mark"></span>torvane</div>
      <p class="brand__tag">A GroomHaven for Men</p>
    </div>
  </section>
</body>
</html>
```